Electrical Contracting Business Website

Require website done for my contracting business.
Partly done one but really dont have time.

You can view the current one at http://brelton.net.au

You can use any info/styles/photos from the current website

I like the orange color of the logo so id like things to be with that
Unfortunatly being a new business (Sept 2015) I havent got alot of photos . but if you require any for any of the specifics listed in the doc file ill have a look to see what I have.

I am targeting mainly commercial / industrial clients. Which also includes government and mining.

Target Market(s)

People requiring electricians

Industry/Entity Type

Electrician

Coding

Number of Pages Required

Colors
f37122

Requirements
Must have
• logo with EC Number
• Keep it simple and not to complicated
• Comply with the current html / style sheet standards.
• Desktop/Mobile Version compatability
Nice to have
• additional photos.
• The domestic lifts we install are by vostrel I dont have any photos of them unfortunately.
Should not have
• change colour of logo

```html
<!DOCTYPE html>
<html lang="en">
<head>
<meta charset="utf-8">
<title>Brelton Engineering</title>
<link rel="stylesheet" href="https://fonts.googleapis.com/css2?family=Open+Sans:wght@400;600;700&family=Arimo&display=swap">
<style>
:root{
  --orange:#f0582a;
  --ink:#3a3b3f;
  --dark:#3f4045;
  --white:#ffffff;
  --muted:#555;
}
*{box-sizing:border-box;margin:0;padding:0}
html,body{width:1200px;height:1187px;overflow:hidden;background:var(--white)}
body{position:relative;font-family:"Open Sans",sans-serif;color:var(--ink)}
.site-header{position:absolute;left:0;top:0;width:1200px;height:110px;border-bottom:4px solid var(--orange);height:114px}
.brand{position:absolute;left:32px;top:36px;display:flex;align-items:center;gap:10px}
.brand-dot{width:34px;height:34px;border-radius:50%;background:var(--orange)}
.brand-name{font-size:34px;font-weight:700;color:var(--orange);letter-spacing:1px;line-height:1}
.contact-bar{position:absolute;right:20px;top:6px;display:flex;gap:34px;font-size:13px;color:var(--muted)}
.contact-bar span{display:flex;align-items:center;gap:7px}
.contact-bar svg{width:13px;height:13px;fill:var(--orange)}
.main-nav{position:absolute;right:19px;top:43px;display:flex;gap:34px;font-size:16px;color:var(--ink)}
.main-nav a{color:inherit;text-decoration:none;padding:0 5px;line-height:22px}
.main-nav a.active{background:var(--orange);color:var(--white)}
.hero{position:absolute;left:0;top:114px;width:1200px;height:512px;
  background:linear-gradient(100deg,#c9cdd2 0%,#9ea6ad 30%,#7f8a93 55%,#6e6a66 75%,#8a7565 100%)}
.hero-title{position:absolute;left:0;width:1200px;text-align:center;color:var(--white);font-weight:700;line-height:1}
.hero-title.big{top:112px;font-size:82px;letter-spacing:1px;padding-left:0}
.hero-title.small{top:194px;font-size:64px;font-weight:600;left:-25px}
.hero-btn{position:absolute;left:489px;top:281px;width:178px;height:51px;background:var(--orange);color:var(--white);
  border-radius:3px;font-size:19px;display:flex;align-items:center;justify-content:center}
.slider-dots{position:absolute;top:438px;left:551px;display:flex;gap:15px}
.slider-dots i{width:10px;height:10px;border-radius:50%;background:var(--orange);display:block}
.slider-dots i.current{background:var(--ink);border:2px solid var(--orange)}
.welcome h1{position:absolute;top:674px;left:0;width:1200px;text-align:center;font-size:34px;font-weight:600;color:var(--ink)}
.welcome h1 em{font-style:normal;color:var(--orange)}
.welcome p{position:absolute;top:746px;width:400px;font-family:"Arimo",sans-serif;font-size:14.4px;line-height:18px;letter-spacing:1px;color:#222}
.welcome .col-left{left:140px}
.welcome .col-right{left:658px}
.services{position:absolute;left:0;top:914px;width:1200px;height:273px;background:var(--dark)}
.services h2{position:absolute;top:23px;width:1200px;text-align:center;color:var(--white);font-size:32px;font-weight:600}
.service{position:absolute;top:88px;width:240px;margin-left:-120px;text-align:center;color:var(--white)}
.service .icon{width:96px;height:96px;border-radius:50%;background:var(--orange);margin:0 auto;display:flex;align-items:center;justify-content:center}
.service .icon svg{width:54px;height:54px;fill:var(--white)}
.service h3{font-weight:400;font-size:23px;line-height:27px;margin-top:16px}
</style>
</head>
<body>
<header class="site-header">
  <div class="brand"><div class="brand-dot"></div><div class="brand-name">BRELTON</div></div>
  <div class="contact-bar">
    <span><svg viewBox="0 0 24 24"><path d="M6.6 10.8a15.2 15.2 0 0 0 6.6 6.6l2.2-2.2c.3-.3.7-.4 1-.2 1.1.4 2.3.6 3.6.6.6 0 1 .4 1 1V20c0 .6-.4 1-1 1A17 17 0 0 1 3 4c0-.6.4-1 1-1h3.5c.6 0 1 .4 1 1 0 1.3.2 2.5.6 3.6.1.3 0 .7-.2 1z"/></svg>+61 0400 217 386</span>
    <span><svg viewBox="0 0 24 24"><path d="M5 3h10v5h4v13H5zM7 10h3v2H7zm5 0h3v2h-3zM7 14h3v2H7zm5 0h3v2h-3zM7 5v3h6V5z"/></svg>+61 (08) 6100 4272</span>
    <span><svg viewBox="0 0 24 24"><path d="M2 5h20v14H2zm2 2v1l8 5 8-5V7l-8 5z"/></svg>info@brelton.net.au</span>
  </div>
  <nav class="main-nav">
    <a class="active">HOME</a><a>ABOUT US</a><a>RESINDENTIAL</a><a>COMMERCIAL</a><a>INDUSTRIAL</a><a>CONTACT US</a>
  </nav>
</header>

<section class="hero" role="img" aria-label="Photo of an electrician's hands working with a screwdriver on a switchboard">
  <div class="hero-title big">COMMERCIAL</div>
  <div class="hero-title small">SERVICE</div>
  <div class="hero-btn">KNOW MORE</div>
  <div class="slider-dots"><i></i><i class="current"></i><i></i><i></i></div>
</section>

<section class="welcome">
  <h1>Welcome to <em>Brelton Engineering</em></h1>
  <p class="col-left">The main body should clearly state the points that you want to make. As a general rule it is good idea to keep this as to the point as possible to ensure that the recipient remains engaged. A longer main body may be more appropriate when making a complaint as you may require to add-more detail in order to convey</p>
  <p class="col-right">The main body should clearly state the points that you want to make. As a general rule it is good idea to keep this as to the point as possible to ensure that the recipient remains engaged.</p>
</section>

<section class="services">
  <h2>What We DO ?</h2>
  <div class="service" style="left:292px">
    <div class="icon"><svg viewBox="0 0 24 24"><path d="M12 3 1 12l1.3 1.5L4 12v9h6v-6h4v6h6v-9l1.7 1.5L23 12zm0 2.6 6 5V19h-2v-6H8v6H6v-8.4z"/></svg></div>
    <h3>Residential<br>Services</h3>
  </div>
  <div class="service" style="left:600px">
    <div class="icon"><svg viewBox="0 0 24 24"><path d="M5 2h9v4h5v16H5zm2 2v2h2V4zm3 0v2h2V4zM7 8v2h2V8zm3 0v2h2V8zm4 0v2h2V8zM7 12v2h2v-2zm3 0v2h2v-2zm4 0v2h2v-2zM7 16v2h2v-2zm7 0v2h2v-2zm-4 0v5h2v-5z"/></svg></div>
    <h3>Commercial<br>Services</h3>
  </div>
  <div class="service" style="left:907px">
    <div class="icon"><svg viewBox="0 0 24 24"><path d="M17 4h3v17H2V11l5 3v-3l5 3v-3l5 3zM4 16v2h3v-2zm5 0v2h3v-2zm5 0v2h3v-2zM17 1h3v2h-3z"/></svg></div>
    <h3>Industrial<br>Services</h3>
  </div>
</section>
</body>
</html>
```